Brindle Lawyers Banner

I would like to have a graphic design created for a company banner. The company is Brindle Lawyers and the website is https://brindlelawyers.example.au/ We would like a professional banner we are able to put up at events to advertise the company.
The banner size is 800mm wide by 2000mm high so please keep the design inside these constraints.

```html
<!DOCTYPE html>
<html lang="en">
<head>
<meta charset="utf-8">
<title>Brindle Lawyers – Event Banner</title>
<link rel="stylesheet" href="https://fonts.googleapis.com/css2?family=Montserrat:wght@300;400;500;700;800&family=Nunito:wght@600;700&display=swap">
<style>
  :root {
    --charcoal: #2e3135;
    --brand-blue: #1f8fd0;
    --bright-blue: #2aa7e0;
    --deep-blue: #1a6fb0;
    --tick-teal: #19a9cf;
    --ink: #2c2f33;
    --paper: #ffffff;
    --mist: #e6e9ec;
    --rule: #d4d8dc;
    --backdrop: #d9dadc;
    --pin-red: #e8232f;
    --badge: #3b4046;
  }
  * { box-sizing: border-box; margin: 0; padding: 0; }
  html, body { width: 1200px; height: 2486px; overflow: hidden; }
  body { background: var(--backdrop); font-family: "Montserrat", sans-serif; color: var(--ink); }

  .banner { position: absolute; left: 120px; top: 43px; width: 960px; height: 2400px; background: var(--paper); overflow: hidden; box-shadow: 0 20px 40px rgba(0,0,0,.25); }
  .banner > * { position: absolute; }

  .shapes { left: 0; top: 0; width: 960px; height: 2400px; }

  .hero-photo { left: 0; top: 372px; width: 960px; height: 782px;
    background: linear-gradient(160deg, var(--bright-blue) 0%, var(--brand-blue) 50%, var(--deep-blue) 100%); }

  .brand { left: 0; width: 960px; top: 130px; text-align: center; color: var(--paper); font-weight: 300; }
  .brand-name { display: block; font-size: 118px; letter-spacing: 6px; line-height: 1; }
  .brand-sub { display: block; font-size: 40px; letter-spacing: 10px; margin-top: 10px; padding-left: 300px; }

  .headline { left: 0; width: 960px; top: 500px; text-align: center; color: var(--paper); font-weight: 300; line-height: 1; }
  .headline-top { display: block; font-size: 100px; letter-spacing: 2px; }
  .headline-main { display: block; font-size: 134px; margin-top: 4px; letter-spacing: 2px; }

  .pin { left: 452px; top: 770px; width: 56px; height: 84px; }
  .address-box { left: 252px; top: 839px; width: 447px; height: 254px; border: 3px solid var(--charcoal); border-radius: 26px;
    display: flex; align-items: center; justify-content: center; text-align: center;
    font-family: "Nunito", sans-serif; font-weight: 700; font-size: 43px; line-height: 50px; color: var(--paper); }

  .section-title { left: 0; width: 960px; text-align: center; font-weight: 800; letter-spacing: -0.5px; }
  .specialising-title { top: 1176px; color: var(--paper); font-size: 46px; }

  .service-list { list-style: none; font-size: 30px; line-height: 35px; color: var(--ink); }
  .service-list li { position: relative; padding-left: 36px; margin-bottom: 35px; }
  .service-list li svg { position: absolute; left: 0; top: 6px; width: 24px; height: 24px; }
  .service-list.left { left: 102px; top: 1303px; width: 360px; }
  .service-list.right { left: 545px; top: 1303px; width: 360px; }
  .col-divider { left: 476px; top: 1290px; width: 3px; height: 430px; background: var(--rule); }

  .help-title { top: 1770px; font-size: 42px; color: var(--ink); }
  .help-title em { font-style: normal; color: var(--brand-blue); }
  .help-dots { left: 450px; top: 1828px; width: 60px; height: 12px; }

  .audience { left: 0; top: 1855px; width: 960px; display: flex; justify-content: center; }
  .audience-item { width: 208px; text-align: center; font-size: 24px; font-weight: 700; line-height: 29px; color: var(--ink); border-right: 3px solid var(--rule); }
  .audience-item:last-child { border-right: none; }
  .audience-item svg { width: 72px; height: 72px; display: block; margin: 0 auto 12px; }

  .contact { left: 92px; top: 2120px; color: var(--paper); }
  .contact-row { display: flex; align-items: center; gap: 12px; font-size: 26px; margin-bottom: 16px; }
  .contact-row svg { width: 24px; height: 24px; flex: none; }
  .contact-row.phone { font-size: 40px; font-weight: 500; margin-bottom: 14px; }
  .contact-row.phone svg { width: 30px; height: 30px; }
  .contact-row.address { align-items: flex-start; font-size: 20px; line-height: 24px; }
  .footer-divider { left: 543px; top: 2090px; height: 250px; border-left: 3px dashed #6b7077; }
  .partner-badge { left: 650px; top: 2127px; width: 198px; height: 186px; background: var(--badge); border-radius: 10px; }
</style>
</head>
<body>
<main class="banner">
  <div class="hero-photo" role="img" aria-label="Photograph of a lawyer working at a desk with laptop and documents, tinted blue"></div>

  <svg class="shapes" viewBox="0 0 960 2400" aria-hidden="true">
    <!-- header -->
    <polygon points="0,0 960,0 960,442 72,442 0,372" fill="var(--charcoal)"/>
    <polyline points="0,120 100,120 115,105 115,0" fill="none" stroke="var(--brand-blue)" stroke-width="4"/>
    <polyline points="0,100 90,100 90,0" fill="none" stroke="var(--brand-blue)" stroke-width="3"/>
    <polygon points="815,325 960,325 960,442 860,442 815,400" fill="var(--brand-blue)"/>
    <polygon points="870,442 870,380 960,380 960,442" fill="var(--charcoal)"/>
    <polygon points="880,442 960,380 960,442" fill="var(--brand-blue)"/>
    <!-- specialising band -->
    <polygon points="0,1090 80,1154 880,1154 960,1090 960,1185 880,1253 80,1253 0,1185" fill="var(--charcoal)"/>
    <polyline points="845,1150 845,1280 780,1290" fill="none" stroke="#c9ced3" stroke-width="3"/>
    <polyline points="875,1160 875,1300 820,1320 820,1340" fill="none" stroke="#c9ced3" stroke-width="3"/>
    <polygon points="935,1337 960,1337 960,1558 905,1558 905,1360" fill="var(--mist)"/>
    <!-- help section -->
    <polygon points="0,1800 60,1730 900,1730 960,1790 960,2070 0,2070" fill="var(--mist)"/>
    <polyline points="0,1820 70,1820 70,1920" fill="none" stroke="#c9ced3" stroke-width="3"/>
    <!-- footer -->
    <polygon points="0,2135 65,2070 895,2070 960,2135 960,2400 0,2400" fill="var(--charcoal)"/>
  </svg>

  <h1 class="brand">
    <span class="brand-name">BRINDLE</span>
    <span class="brand-sub">LAWYERS</span>
  </h1>

  <h2 class="headline">
    <span class="headline-top">COMMERCIAL</span>
    <span class="headline-main">LAW FIRM</span>
  </h2>

  <svg class="pin" viewBox="0 0 56 84" aria-hidden="true">
    <ellipse cx="28" cy="76" rx="26" ry="7" fill="var(--charcoal)"/>
    <path d="M28 2 C13 2 4 13 4 26 C4 44 28 72 28 72 C28 72 52 44 52 26 C52 13 43 2 28 2Z" fill="var(--pin-red)"/>
    <circle cx="28" cy="25" r="9" fill="#fff"/>
  </svg>
  <p class="address-box">Unit 8 Harbour<br>Court, 412<br>Ridge Road,<br>Eastvale</p>

  <h3 class="section-title specialising-title">SPECIALISING IN</h3>

  <ul class="service-list left">
    <li><svg viewBox="0 0 24 24"><circle cx="12" cy="12" r="11" fill="var(--tick-teal)"/><path d="M7 12.5l3.5 3.5L17 9" fill="none" stroke="#fff" stroke-width="2.6"/></svg>Advising Family Businesses</li>
    <li><svg viewBox="0 0 24 24"><circle cx="12" cy="12" r="11" fill="var(--tick-teal)"/><path d="M7 12.5l3.5 3.5L17 9" fill="none" stroke="#fff" stroke-width="2.6"/></svg>Estate Planning, Administration and Disputes</li>
    <li><svg viewBox="0 0 24 24"><circle cx="12" cy="12" r="11" fill="var(--tick-teal)"/><path d="M7 12.5l3.5 3.5L17 9" fill="none" stroke="#fff" stroke-width="2.6"/></svg>Tax and Structuring</li>
    <li><svg viewBox="0 0 24 24"><circle cx="12" cy="12" r="11" fill="var(--tick-teal)"/><path d="M7 12.5l3.5 3.5L17 9" fill="none" stroke="#fff" stroke-width="2.6"/></svg>Planning and Environment</li>
  </ul>
  <div class="col-divider"></div>
  <ul class="service-list right">
    <li><svg viewBox="0 0 24 24"><circle cx="12" cy="12" r="11" fill="var(--tick-teal)"/><path d="M7 12.5l3.5 3.5L17 9" fill="none" stroke="#fff" stroke-width="2.6"/></svg>Not for Profit and Social Enterprise</li>
    <li><svg viewBox="0 0 24 24"><circle cx="12" cy="12" r="11" fill="var(--tick-teal)"/><path d="M7 12.5l3.5 3.5L17 9" fill="none" stroke="#fff" stroke-width="2.6"/></svg>Management Rights, Property and Developments</li>
    <li><svg viewBox="0 0 24 24"><circle cx="12" cy="12" r="11" fill="var(--tick-teal)"/><path d="M7 12.5l3.5 3.5L17 9" fill="none" stroke="#fff" stroke-width="2.6"/></svg>Litigation and Dispute Resolution</li>
  </ul>

  <h3 class="section-title help-title">HOW CAN WE <em>HELP YOU?</em></h3>
  <svg class="help-dots" viewBox="0 0 60 12" aria-hidden="true">
    <circle cx="6" cy="6" r="4.5" fill="#7a7f85"/><circle cx="22" cy="6" r="4.5" fill="#7a7f85"/><circle cx="38" cy="6" r="4.5" fill="#a8adb2"/><circle cx="54" cy="6" r="4.5" fill="#c9ced3"/>
  </svg>

  <div class="audience">
    <div class="audience-item">
      <svg viewBox="0 0 72 72" fill="none" stroke="var(--brand-blue)" stroke-width="3"><path d="M14 6h30l10 10v50H14z"/><path d="M22 24h22M22 32h22M22 40h16M22 48h12"/><path d="M62 26L42 54l-6 4 2-7 20-28z"/></svg>
      Private clients<br>and family<br>business
    </div>
    <div class="audience-item">
      <svg viewBox="0 0 72 72" fill="none" stroke="var(--brand-blue)" stroke-width="3"><path d="M64 8C48 8 34 18 26 34l12 12c16-8 26-22 26-38z"/><circle cx="48" cy="24" r="5"/><path d="M26 34l-12 2-6 8 14 2M38 46l-2 12-8 6-2-14"/><path d="M20 52l-10 10"/></svg>
      Start-up<br>and New<br>business
    </div>
    <div class="audience-item">
      <svg viewBox="0 0 72 72" fill="none" stroke="var(--brand-blue)" stroke-width="3"><circle cx="36" cy="12" r="6"/><path d="M28 28c0-5 16-5 16 0"/><path d="M36 30v10M14 40h44M14 40v8M36 40v8M58 40v8"/><circle cx="14" cy="56" r="6"/><circle cx="36" cy="56" r="6"/><circle cx="58" cy="56" r="6"/></svg>
      Eshtablished<br>organisations
    </div>
    <div class="audience-item">
      <svg viewBox="0 0 72 72" fill="none" stroke="var(--brand-blue)" stroke-width="3"><rect x="20" y="4" width="34" height="20" rx="6"/><path d="M30 24l-4 6 10-6"/><circle cx="18" cy="42" r="6"/><path d="M6 66c0-10 24-10 24 0z"/><circle cx="52" cy="42" r="6"/><path d="M40 66c0-10 24-10 24 0z"/></svg>
      Professional<br>advisors
    </div>
  </div>

  <address class="contact" style="font-style:normal">
    <p class="contact-row phone"><svg viewBox="0 0 24 24" fill="none" stroke="var(--tick-teal)" stroke-width="2.2"><path d="M5 3h4l2 5-2.5 1.5a11 11 0 0 0 6 6L16 13l5 2v4a2 2 0 0 1-2 2A16 16 0 0 1 3 5a2 2 0 0 1 2-2z"/></svg>07 5550 1482</p>
    <p class="contact-row"><svg viewBox="0 0 24 24"><rect x="2" y="5" width="20" height="14" fill="var(--tick-teal)"/><path d="M2 5l10 8 10-8" fill="none" stroke="var(--charcoal)" stroke-width="1.8"/></svg>info@brindlelawyers.example.au</p>
    <p class="contact-row"><svg viewBox="0 0 24 24" fill="none" stroke="var(--tick-teal)" stroke-width="2"><circle cx="12" cy="12" r="10"/><path d="M2 12h20M12 2c4 4 4 16 0 20M12 2c-4 4-4 16 0 20"/></svg>www.brindlelawyers.example.au</p>
    <p class="contact-row address"><svg viewBox="0 0 24 24"><path d="M12 1C7 1 4 5 4 9c0 6 8 14 8 14s8-8 8-14c0-4-3-8-8-8z" fill="var(--tick-teal)"/><circle cx="12" cy="9" r="3" fill="var(--charcoal)"/></svg>Unit 8 Harbour Court, 412 Ridge Road,<br>Eastvale</p>
  </address>
  <div class="footer-divider"></div>
  <div class="partner-badge" role="img" aria-label="Partner accreditation badge"></div>
</main>
</body>
</html>
```